Book cover for LS

Design cover for a book of gratitude and inspiration.
Book trim size will be 6.5 x 6.5 inches, or 8 x 8 inches, hardcover, 96 pages
Title: Lantern Stones
Subtitle: A Book of Gratitude and Inspiration
Author: Carl Wendover

```html
<!DOCTYPE html>
<html lang="en">
<head>
<meta charset="utf-8">
<title>Lantern Stones – Cover</title>
<link href="https://fonts.googleapis.com/css2?family=Cinzel:wght@400;700&family=Montserrat:wght@400;600&display=swap" rel="stylesheet">
<style>
  :root{
    --page:#ececec;
    --cover:#2b313b;
    --cover-deep:#232831;
    --ink:#ffffff;
    --sage:#8fbf8e;
    --mint:#cfe6d8;
    --mint-mid:#8fb3a6;
    --body:#e8ebee;
  }
  html,body{margin:0;padding:0;width:1200px;height:1189px;overflow:hidden;background:var(--page);}
  .jacket{position:absolute;left:49px;top:327px;width:1102px;height:534px;background:var(--cover);overflow:hidden;}
  .serif{font-family:"Cinzel",serif;}
  .back-subtitle{position:absolute;left:105px;top:46px;width:325px;text-align:center;font-size:14px;color:var(--sage);font-family:"Cinzel",serif;white-space:nowrap;}
  .back-title{position:absolute;left:100px;top:62px;width:336px;text-align:center;color:var(--ink);font-family:"Cinzel",serif;font-size:48px;line-height:44px;}
  .back-title span{display:block}
  .back-title .line2{font-size:58px;line-height:48px}
  .blurb{position:absolute;left:64px;top:159px;width:407px;font-family:"Montserrat",sans-serif;font-size:7.6px;line-height:13.3px;color:var(--body);text-align:justify;}
  .blurb p{margin:0 0 3px}
  .rule{position:absolute;left:64px;top:374px;width:405px;height:2px;background:var(--sage);}
  .author-photo{position:absolute;left:62px;top:382px;width:56px;height:66px;}
  .about{position:absolute;left:126px;top:381px;width:340px;font-family:"Montserrat",sans-serif;font-size:7.6px;line-height:11.5px;color:var(--body);text-align:justify;}
  .about b{font-weight:600}
  .spine{position:absolute;left:514px;top:0;width:60px;height:534px;}
  .spine-text{position:absolute;left:50%;top:40px;transform-origin:0 0;transform:rotate(90deg) translateY(-50%);white-space:nowrap;font-family:"Cinzel",serif;font-size:25px;color:var(--ink);}
  .spine-text .spine-author{color:var(--sage);font-size:19px;margin-left:14px}
  .art{position:absolute;left:640px;top:80px;width:462px;height:454px;}
  .front-subtitle{position:absolute;left:600px;top:14px;width:480px;text-align:center;font-family:"Cinzel",serif;font-size:19.5px;color:var(--sage);white-space:nowrap;}
  .front-title{position:absolute;left:594px;top:35px;width:490px;text-align:center;color:var(--ink);font-family:"Cinzel",serif;text-shadow:2px 2px 1px #000;}
  .front-title span{display:block;font-size:64px;line-height:62px}
  .front-title .line2{font-size:78px;line-height:62px}
  .author-band{position:absolute;left:574px;top:462px;width:528px;height:52px;background:rgba(35,40,49,.85);}
  .front-author{position:absolute;left:574px;top:466px;width:528px;text-align:center;font-family:"Cinzel",serif;font-size:30px;color:var(--ink);text-shadow:1px 1px 1px #000;}
</style>
</head>
<body>
<div class="jacket">
  <!-- back cover -->
  <div class="back-subtitle">A Book of Gratitude and Inspiration</div>
  <h1 class="back-title" style="margin:0;font-weight:400"><span>LANTERN</span><span class="line2">STONES</span></h1>
  <div class="blurb">
    <p>Lorem ipsum dolor sit amet, consectetur adipiscing elit, sed do eiusmod tempor incididunt ut labore et dolore magna aliqua. Erat velit scelerisque in dictum non. Mus mauris vitae ultricies leo integer malesuada nunc. Sed vulputate odio ut enim. Viverra nam libero justo laoreet sit amet cursus sit amet. Neque laoreet suspendisse interdum consectetur libero id faucibus nisl. Semper feugiat nibh sed pulvinar proin gravida hendrerit lectus. Aliquam sem et tortor consequat id. Pulvinar neque laoreet suspendisse interdum consectetur libero id faucibus. Posuere lorem ipsum dolor sit. Cras tincidunt lobortis feugiat vivamus at augue. Quis eleifend quam adipiscing vitae proin. Sit amet consectetur.</p>
    <p>Id venenatis a condimentum vitae. Massa placerat duis ultricies lacus. Eleifend donec pretium vulputate sapien nec. Molestie nunc non blandit massa enim nec. Donec pretium vulputate sapien nec sagittis aliquam malesuada bibendum arcu. Nibh ipsum consequat nisl vel. Nulla malesuada pellentesque elit eget. Proin sagittis nisl rhoncus mattis rhoncus urna neque viverra justo. Lectus proin nibh nisl condimentum id venenatis. Cursus sit amet dictum sit amet justo donec. Scelerisque varius morbi enim nunc faucibus a. Scelerisque viverra mauris in aliquam sem fringilla ut morbi tincidunt. Ultrices gravida dictum fusce ut placerat orci nulla. Diam donec adipiscing tristique risus nec feugiat in. Integer quis auctor elit sed vulputate mi sit amet mauris.</p>
  </div>
  <div class="rule"></div>
  <svg class="author-photo" viewBox="0 0 56 66" role="img" aria-label="Author photo placeholder">
    <rect x="0.5" y="0.5" width="55" height="65" fill="#ffffff" stroke="#9a9a9a"/>
    <line x1="0.5" y1="0.5" x2="55.5" y2="65.5" stroke="#9a9a9a"/>
    <line x1="55.5" y1="0.5" x2="0.5" y2="65.5" stroke="#9a9a9a"/>
  </svg>
  <div class="about"><b>About the Author:</b> Amet commodo nulla facilisi nullam vehicula. Eu augue ut lectus arcu bibendum at varius. Dignissim convallis aenean et tortor at risus. Senectus et netus et malesuada. Id velit ut tortor pretium viverra suspendisse potenti nullam ac. Pretium nibh ipsum consequat nisl vel pretium lectus. Id velit ut tortor pretium viverra suspendisse potenti nullam ac. Pretium nibh ipsum consequat nisl vel pretium lectus.</div>

  <!-- spine -->
  <div class="spine">
    <div class="spine-text">LANTERN STONES<span class="spine-author">CARL WENDOVER</span></div>
  </div>

  <!-- front cover -->
  <svg class="art" viewBox="0 0 462 454" role="img" aria-label="Painted illustration: a pale head silhouette opening onto a staircase with a small figure standing at its foot">
    <defs>
      <radialGradient id="glow" cx="0.55" cy="0.5" r="0.55">
        <stop offset="0" stop-color="#cfe6d8"/>
        <stop offset="0.6" stop-color="#9ec2b2"/>
        <stop offset="1" stop-color="#2b313b" stop-opacity="0"/>
      </radialGradient>
    </defs>
    <ellipse cx="250" cy="220" rx="230" ry="250" fill="url(#glow)"/>
  </svg>
  <div class="front-subtitle">A Book of Gratitude and Inspiration</div>
  <h2 class="front-title" style="margin:0;font-weight:400"><span>LANTERN</span><span class="line2">STONES</span></h2>
  <div class="author-band"></div>
  <div class="front-author">CARL WENDOVER</div>
</div>
</body>
</html>
```